sign business needs card design

I need a very clean design for my business card.
It is a sign company. Banners By Noon is the name of the business.
Our colors are orange, yellow. But I want a very professional card.
But you can use any colors. I like a black background with orange letters or a white back with a clean look. No cartoon or kiddy looking print. The info. I need on the card is as follows.
Banners By Noon
318.514.7702 ph.
318.514.7739 fax.
email.bannersbynoon@velmora.net
web.bannersbynooninc.example
4172 N. Calloway Ridge Ste. 2b
Dale Kessner

```html
<!DOCTYPE html>
<html lang="en">
<head>
<meta charset="utf-8">
<title>Banners By Noon — Business Card</title>
<link href="https://fonts.googleapis.com/css2?family=Alfa+Slab+One&family=BenchNine:wght@400;700&display=swap" rel="stylesheet">
<style>
  :root {
    --page: #ffffff;
    --stage-top: #232d34;
    --stage-bottom: #1c252b;
    --card: #832b2e;
    --title: #ffffff;
    --info: #f1d9d9;
    --rule: rgba(255, 255, 255, 0.28);
  }
  html, body {
    margin: 0;
    padding: 0;
    width: 1200px;
    height: 686px;
    overflow: hidden;
    background: var(--page);
  }
  .stage {
    position: absolute;
    left: 1px;
    top: 1px;
    width: 1198px;
    height: 684px;
    border-radius: 14px;
    background: linear-gradient(160deg, var(--stage-top), var(--stage-bottom));
  }
  .card {
    position: absolute;
    left: 375px;
    top: 202px;
    width: 451px;
    height: 282px;
    background: var(--card);
    clip-path: polygon(27px 0, calc(100% - 27px) 0, 100% 27px, 100% calc(100% - 27px), calc(100% - 27px) 100%, 27px 100%, 0 calc(100% - 27px), 0 27px);
  }
  .card-name {
    position: absolute;
    left: 47px;
    top: 34px;
    margin: 0;
    font-family: "Alfa Slab One", serif;
    font-weight: 400;
    font-size: 28px;
    line-height: 1;
    letter-spacing: 0.3px;
    color: var(--title);
    text-transform: uppercase;
  }
  .card-info {
    position: absolute;
    left: 47px;
    top: 69px;
    margin: 0;
    padding: 0;
    list-style: none;
    font-family: "BenchNine", sans-serif;
    font-size: 16px;
    letter-spacing: 0.6px;
    color: var(--info);
    text-transform: uppercase;
  }
  .card-info li {
    height: 27.5px;
    line-height: 22px;
  }
  .card-info .ruled span {
    display: inline-block;
    border-bottom: 1px solid var(--rule);
    padding-bottom: 1px;
  }
</style>
</head>
<body>
  <div class="stage">
    <section class="card" aria-label="Banners By Noon business card">
      <h1 class="card-name">Banners By Noon.</h1>
      <ul class="card-info">
        <li class="ruled"><span>bannersbynooninc.example &nbsp;//</span></li>
        <li>318 - 514 - 7702 &nbsp;ph.</li>
        <li>318 - 514 - 7739 &nbsp;fax.</li>
        <li>email. - bannersbynoon@velmora.net</li>
        <li class="ruled"><span>web. - bannersbynooninc.example</span></li>
        <li>4172 N. Calloway Ridge Ste. 2b</li>
        <li>Dale Kessner</li>
      </ul>
    </section>
  </div>
</body>
</html>
```